Business Card and Simple Logo Desgin

New Zealand based start up company "Brook Advisory LTD" requires business cards and simple logo design.

Card Content.

Brook Advisory LTD

Joanna Pritchard
CA, BMS (Hons)

j.pritchard@brookadvisory.co.nz
PH +64 21 574 160

Target Market(s)

Corporate Business in IT, Finance and accounting.

Industry/Entity Type

Business

```html
<!DOCTYPE html>
<html lang="en">
<head>
<meta charset="utf-8">
<title>Brook Advisory LTD – Business Cards</title>
<link rel="stylesheet" href="https://fonts.googleapis.com/css2?family=Open+Sans:wght@400;700&family=Tinos:wght@400;700&display=swap">
<style>
  :root {
    --stage: #141414;
    --brand-orange: #f5a300;
    --brand-orange-deep: #e08f00;
    --card-white: #ffffff;
    --ink: #3a3a3a;
    --ink-soft: #555555;
    --on-dark: #ffffff;
  }
  * { margin: 0; padding: 0; box-sizing: border-box; }
  html, body { width: 1200px; height: 871px; overflow: hidden; background: var(--stage); }
  .canvas { position: relative; width: 1200px; height: 871px; background: var(--stage); }

  .card {
    position: absolute;
    width: 520px;
    height: 300px;
    top: 90px;
    border-radius: 4px;
  }

  /* Back of card */
  .card--back {
    left: 50px;
    background: linear-gradient(135deg, var(--brand-orange) 0%, var(--brand-orange-deep) 100%);
  }
  .card--back .lockup {
    position: absolute;
    left: 120px;
    top: 92px;
    display: flex;
    align-items: center;
    gap: 22px;
  }
  .card--back .lockup-dot { width: 96px; height: 96px; border-radius: 50%; background: rgba(255,255,255,0.55); }
  .card--back .lockup-name {
    font-family: "Tinos", "Times New Roman", serif;
    font-size: 30px;
    line-height: 1.0;
    color: var(--on-dark);
  }
  .card--back .website {
    position: absolute;
    left: 238px;
    top: 206px;
    font-family: "Tinos", "Times New Roman", serif;
    font-weight: 700;
    font-size: 12px;
    letter-spacing: 3px;
    color: rgba(255,255,255,0.8);
  }

  /* Front of card */
  .card--front { left: 630px; background: var(--card-white); }
  .holder { position: absolute; left: 34px; top: 34px; font-family: "Open Sans", Arial, sans-serif; }
  .holder-name { font-weight: 700; font-size: 24px; color: var(--ink-soft); line-height: 1.1; }
  .holder-credentials { font-size: 14px; color: var(--ink-soft); margin-top: 4px; }

  .contact { position: absolute; left: 30px; top: 136px; font-family: "Open Sans", Arial, sans-serif; }
  .contact-row { display: flex; align-items: center; gap: 12px; font-size: 14px; color: var(--ink); height: 22px; }
  .contact-badge {
    width: 15px; height: 15px; border-radius: 50%;
    background: var(--brand-orange); color: var(--on-dark);
    font-size: 10px; line-height: 15px; text-align: center;
  }
  .card--front .website {
    position: absolute;
    left: 32px;
    top: 232px;
    font-family: "Tinos", "Times New Roman", serif;
    font-weight: 700;
    font-size: 13px;
    letter-spacing: 3.4px;
    color: var(--ink);
  }
  .card--front .lockup {
    position: absolute;
    right: 30px;
    top: 40px;
    display: flex;
    align-items: center;
    gap: 14px;
  }
  .card--front .lockup-dot { width: 70px; height: 70px; border-radius: 50%; background: var(--brand-orange); }
  .card--front .lockup-name {
    font-family: "Tinos", "Times New Roman", serif;
    font-size: 24px;
    line-height: 1.0;
    color: var(--ink);
  }

  /* Standalone logo lockup */
  .brand-lockup {
    position: absolute;
    left: 110px;
    top: 660px;
    display: flex;
    align-items: center;
    gap: 26px;
  }
  .brand-lockup .lockup-dot { width: 130px; height: 130px; border-radius: 50%; background: var(--brand-orange); }
  .brand-lockup .lockup-name {
    font-family: "Tinos", "Times New Roman", serif;
    font-size: 40px;
    line-height: 1.0;
    color: var(--on-dark);
  }
</style>
</head>
<body>
<main class="canvas">

  <section class="card card--back" aria-label="Business card, back">
    <div class="lockup">
      <span class="lockup-dot"></span>
      <p class="lockup-name">Brook<br>Advisory<br>LTD</p>
    </div>
    <p class="website">www.brookadvisory.co.nz</p>
  </section>

  <section class="card card--front" aria-label="Business card, front">
    <div class="holder">
      <p class="holder-name">Joanna Pritchard</p>
      <p class="holder-credentials">CA, BMS (Hons)</p>
    </div>
    <div class="contact">
      <p class="contact-row"><span class="contact-badge">e</span>j.pritchard@brookadvisory.co.nz</p>
      <p class="contact-row"><span class="contact-badge">m</span>+64 21 574 160</p>
    </div>
    <p class="website">www.brookadvisory.co.nz</p>
    <div class="lockup">
      <span class="lockup-dot"></span>
      <p class="lockup-name">Brook<br>Advisory<br>LTD</p>
    </div>
  </section>

  <div class="brand-lockup">
    <span class="lockup-dot"></span>
    <p class="lockup-name">Brook<br>Advisory<br>LTD</p>
  </div>

</main>
</body>
</html>
```